Kx7Orbit WebSite

an educational website about tutoring, client will be surfing this site looking for a tutor, please see the attached images because the contains exactly what we need.
Updates

Project Deadline Extended Reason: something went wrong with the uploaded files, we are very sorry.thank you PlumeVault for the 5 days extension.now there is a 3 images describing the content of the three pages.good luck Added Friday, August 5, 2016

Target Market(s)

everyone

Industry/Entity Type

Education

Number of Pages Required

3 page

Font styles to use
Other font styles liked:
• something looks good in Arabic and english like "Droid Arabic Kufi"

Requirements
Must have
• the logo we attached, responsive design, simple, also try as much as you can Centering texts and layout because this website will have an Arabic version, Arabic is a Right-to-Left Language.
• a change language button,
Nice to have
• educational gestures.
• Centered texts and layout because this website will have an Arabic version, Arabic is a Right-to-Left Language.
• we have a web designer and we can download any template and add our logo and text to it, but.....
• we need creativity, so please stick to the contents in the images we attached, we need something very simple, more like a zorvia home page with little touch of filtering fields like the 5 dropdownlist and the gender selection buttons.
• try not to go far away from the contents we specified in the images, use less images or dont use images at all, try not to make the client scroll down,
Should not have
• too much colors or noisy layout or heavy media

```html
<!DOCTYPE html>
<html lang="en">
<head>
<meta charset="utf-8">
<title>Kx7Orbit – Personalized Tutoring</title>
<link href="https://fonts.googleapis.com/css2?family=Lato:wght@300;400;700;900&display=swap" rel="stylesheet">
<style>
:root{
  --blue:#1f8fd8;
  --blue-dark:#1566b4;
  --sky:#29a3e2;
  --orange:#f26a21;
  --green:#7dc242;
  --navy:#18415f;
  --ink:#333;
  --muted:#666;
  --pale:#eaf5fc;
  --line:#c8d6e0;
}
*{box-sizing:border-box;margin:0;padding:0}
html,body{width:1200px;height:3214px;overflow:hidden;background:#fff}
body{position:relative;font-family:'Lato',sans-serif;color:var(--ink)}
.abs{position:absolute}

/* header */
.site-header{top:0;left:0;width:1200px;height:80px;background:#fff}
.brand{left:80px;top:20px;display:flex;align-items:center;gap:8px;font-size:30px;font-weight:700;color:var(--blue)}
.brand-mark{width:34px;height:34px;background:var(--blue);border-radius:4px}
.main-nav{right:80px;top:30px;display:flex;gap:34px;font-size:15px;color:#555}
.main-nav .active{color:var(--blue);border-bottom:2px solid var(--blue);padding-bottom:8px}

/* hero */
.hero{top:80px;left:0;width:1200px;height:540px;background:linear-gradient(90deg,#f6f6f4 0%,#efece6 40%,#d9d2c8 100%)}
.hero-photo{top:80px;left:360px;width:840px;height:540px;background:linear-gradient(100deg,rgba(240,238,234,0) 0%,#d8cfc4 35%,#bfb3a5 70%,#e6e0d8 100%)}
.hero-title{left:80px;top:210px;font-size:56px;font-weight:700;color:var(--blue-dark)}
.hero-tagline{left:80px;top:285px;font-size:50px;font-weight:300;line-height:1.1;color:#222}
.btn{display:inline-flex;align-items:center;justify-content:center;background:var(--orange);color:#fff;font-size:20px;font-weight:400}
.hero-cta{left:80px;top:422px;width:235px;height:50px;border:1px solid #c9541a}

/* intro band */
.intro{top:620px;left:0;width:1200px;height:130px;background:var(--sky);text-align:center}
.intro h2{margin-top:24px;font-size:34px;font-weight:400;color:#fff}
.intro p{margin:8px auto 0;width:1000px;font-size:17px;line-height:1.35;color:#c6f08e}
.intro-notch{top:748px;left:582px}

/* section titles */
.section-title{left:0;width:1200px;text-align:center;font-size:31px;font-weight:400;color:var(--blue)}
.title-rule{left:470px;width:260px;height:2px;background:var(--line)}
.title-dot{left:592px;width:16px;height:8px;background:var(--orange);border-radius:8px 8px 0 0}

/* services */
.service{width:250px;text-align:center}
.service svg{display:block;margin:0 auto}
.service h3{margin-top:12px;font-size:18px;font-weight:400;color:#333}
.service p{margin-top:12px;font-size:12px;line-height:1.45;color:#555}
.service a{display:block;margin-top:14px;font-size:13px;text-decoration:none}
.link-green{color:var(--green)}
.link-orange{color:var(--orange)}

/* promo */
.promo{top:1195px;left:0;width:1200px;height:445px;background:linear-gradient(90deg,#fff3ec 0%,#fde4d4 40%,#f7d9c4 100%)}
.promo-photo{top:1195px;left:400px;width:800px;height:445px;background:linear-gradient(110deg,rgba(248,220,200,0) 0%,#a9b0b6 25%,#7d8a97 55%,#c9b7a8 100%)}
.promo-copy{left:80px;top:1270px;line-height:1}
.promo-copy .l1{font-size:40px;font-weight:300;color:var(--blue)}
.promo-copy .l2{margin-top:12px;font-size:60px;font-weight:700;color:var(--blue-dark)}
.promo-copy .l3{margin-top:12px;font-size:40px;font-weight:300;color:var(--orange)}
.promo-copy .l4{margin-top:12px;font-size:60px;font-weight:700;color:var(--orange)}
.role-btn{top:1518px;height:38px;font-size:15px;padding:0 14px;gap:8px}
.role-btn.student{left:80px;background:var(--blue-dark)}
.role-btn.tutor{left:243px;background:var(--orange)}

/* testimonials */
.quote{left:80px;top:1760px;width:1040px;text-align:center;font-size:14px;line-height:1.6;color:#555;padding:0 40px}
.quote-mark{font-size:60px;font-weight:900;color:var(--green);line-height:1}
.name-tag{left:500px;top:1848px;width:200px;height:48px;background:var(--orange);color:#fff;text-align:center;padding-top:6px}
.name-tag strong{display:block;font-size:16px;font-weight:400}
.name-tag span{font-size:11px}
.avatar{border-radius:50%}

/* articles */
.posts{top:2135px;left:0;width:1200px;height:425px;background:var(--pale)}
.post-col{top:2180px;width:490px}
.post-col h3{font-size:22px;font-weight:400;color:#333;padding-bottom:12px;border-bottom:2px solid var(--line);position:relative}
.pager{position:absolute;right:0;top:2px;font-size:22px;color:#f3b48e;letter-spacing:4px}
.post{display:flex;gap:20px;margin-top:30px}
.thumb{width:78px;height:78px;border:6px solid var(--navy);flex:none}
.post h4{font-size:14px;font-weight:700;color:#222}
.post p{margin-top:8px;font-size:11.5px;line-height:1.4;color:#444}
.post .by{margin-top:8px;font-size:11.5px;color:#444}

/* partners */
.partner{top:2695px;width:170px;height:97px;border:1px solid #ccc;background:#fff;display:flex;align-items:center;justify-content:center}
.partner span{display:block;width:110px;height:46px;border-radius:6px;background:#d7dde3}
.carousel-arrow{top:2725px;font-size:40px;color:#999;font-weight:300}

/* footer */
.site-footer{top:2890px;left:0;width:1200px;height:282px;background:var(--blue-dark)}
.foot-col{top:2938px;color:#fff}
.foot-col h4{font-size:17px;font-weight:400;color:#bfe0f7;padding-bottom:10px;border-bottom:1px solid #3f86c8;width:200px}
.foot-col ul{list-style:none;margin-top:14px;font-size:12.5px;line-height:1.55}
.foot-col li::before{content:"• ";}
.contact-row{display:flex;gap:12px;margin-top:16px;font-size:12.5px;line-height:1.4}
.newsletter p{margin-top:14px;font-size:12px;line-height:1.4;width:220px}
.newsletter .field{margin-top:12px;width:200px;height:26px;background:#fff;color:#777;font-size:11px;padding:6px 8px}
.newsletter .subscribe{margin-top:18px;height:24px;padding:0 12px;font-size:11px}
.social{display:flex;align-items:center;gap:14px;margin-top:14px;font-size:13px}
.social i{width:22px;height:22px;background:#5aa8e6;display:block;border-radius:3px}
.bottom-bar{top:3172px;left:0;width:1200px;height:42px;background:var(--green);color:#fff;font-size:12px}
.bottom-bar .copy{position:absolute;left:80px;top:14px}
.bottom-bar .links{position:absolute;right:80px;top:14px;display:flex;gap:22px}
</style>
</head>
<body>

<header class="site-header abs">
  <div class="brand abs"><span class="brand-mark"></span>Kx7Orbit</div>
  <nav class="main-nav abs">
    <span class="active">Home</span><span>About</span><span>How It Works</span><span>Students &amp;Parents</span><span>Tutors</span><span>Blog</span><span>Contact Us</span>
  </nav>
</header>

<section class="hero abs"></section>
<div class="hero-photo abs" role="img" aria-label="Young woman studying at a desk with a laptop and notebook"></div>
<h1 class="hero-title abs">Kx7Orbit</h1>
<p class="hero-tagline abs">Personalized Tutoring<br>For Success.</p>
<a class="btn hero-cta abs">View Our Tutors</a>

<section class="intro abs">
  <h2>Kx7Orbit Is A  UK's No 1 Tutoring Services Provider.</h2>
  <p>Lorem ipsum dolor sit amet, consectetur adipiscing elit. Sed lobortis dui leo, et accumsan lacus tempor blandit. Class aptent taciti sociosqu ad litora torquent per conubia nostra, per inceptos himenaeos.</p>
</section>
<svg class="intro-notch abs" width="36" height="18" viewBox="0 0 36 18"><path d="M0 0H36L18 18Z" fill="#29a3e2"/></svg>

<h2 class="section-title abs" style="top:808px">Our Services</h2>
<div class="title-rule abs" style="top:860px"></div>
<div class="title-dot abs" style="top:852px"></div>

<div class="service abs" style="left:75px;top:900px">
  <svg width="112" height="112" viewBox="0 0 112 112"><circle cx="56" cy="56" r="53" fill="none" stroke="#7dc242" stroke-width="2"/><circle cx="56" cy="56" r="24" fill="none" stroke="#7dc242" stroke-width="3"/><path d="M36 38a28 28 0 0 1 40 0" fill="none" stroke="#7dc242" stroke-width="3"/><text x="56" y="62" text-anchor="middle" font-family="Lato,sans-serif" font-size="16" font-weight="700" fill="#7dc242">24</text></svg>
  <h3>24/7 Access</h3>
  <p>Nullam sit amet scelerisque justo. Nullam at blandit augue, at iaculis erat. Etiam ligula cursus nec.</p>
  <a class="link-green">View Memebership Plans &gt;&gt;</a>
</div>
<div class="service abs" style="left:342px;top:900px">
  <svg width="112" height="112" viewBox="0 0 112 112"><circle cx="56" cy="56" r="53" fill="none" stroke="#f26a21" stroke-width="2"/><circle cx="56" cy="52" r="22" fill="none" stroke="#f26a21" stroke-width="3"/><circle cx="56" cy="52" r="12" fill="none" stroke="#f26a21" stroke-width="2"/><path d="M44 70l-6 16 10-4 6 8 2-18M68 70l6 16-10-4-6 8-2-18" fill="none" stroke="#f26a21" stroke-width="2"/></svg>
  <h3>The Best Tutors</h3>
  <p>Nullam sit amet scelerisque justo. Nullam at blandit augue, at iaculis erat. Etiam ligula cursus nec.</p>
  <a class="link-orange">See our Tutors &gt;&gt;</a>
</div>
<div class="service abs" style="left:608px;top:900px">
  <svg width="112" height="112" viewBox="0 0 112 112"><circle cx="56" cy="56" r="53" fill="none" stroke="#7dc242" stroke-width="2"/><circle cx="54" cy="58" r="24" fill="none" stroke="#7dc242" stroke-width="3"/><circle cx="54" cy="58" r="13" fill="none" stroke="#7dc242" stroke-width="3"/><circle cx="54" cy="58" r="4" fill="#7dc242"/><path d="M54 58L80 32M74 30h8v8" fill="none" stroke="#7dc242" stroke-width="3"/></svg>
  <h3>Personalized</h3>
  <p>Nullam sit amet scelerisque justo. Nullam at blandit augue, at iaculis erat. Etiam ligula cursus nec.</p>
  <a class="link-green">View Students' Testimonials &gt;&gt;</a>
</div>
<div class="service abs" style="left:875px;top:900px">
  <svg width="112" height="112" viewBox="0 0 112 112"><circle cx="56" cy="56" r="53" fill="none" stroke="#f26a21" stroke-width="2"/><circle cx="56" cy="56" r="26" fill="none" stroke="#f26a21" stroke-width="3"/><path d="M56 30v52M30 56h52M38 38l36 36M74 38L38 74" stroke="#f26a21" stroke-width="2"/></svg>
  <h3>Variety Of Subjects</h3>
  <p>Nullam sit amet scelerisque justo. Nullam at blandit augue, at iaculis erat. Etiam ligula cursus nec.</p>
  <a class="link-orange">View All Subjects &gt;&gt;</a>
</div>

<section class="promo abs"></section>
<div class="promo-photo abs" role="img" aria-label="Group of smiling students giving thumbs up in a classroom"></div>
<div class="promo-copy abs">
  <div class="l1">Make The Future</div>
  <div class="l2">Bright</div>
  <div class="l3">&amp; Lets The World</div>
  <div class="l4">Win</div>
</div>
<a class="btn role-btn student abs"><svg width="14" height="16" viewBox="0 0 14 16"><circle cx="7" cy="4" r="3.5" fill="#fff"/><path d="M0 16c0-5 3-7 7-7s7 2 7 7z" fill="#fff"/></svg>I am a Student</a>
<a class="btn role-btn tutor abs"><svg width="14" height="16" viewBox="0 0 14 16"><circle cx="7" cy="4" r="3.5" fill="#fff"/><path d="M0 16c0-5 3-7 7-7s7 2 7 7z" fill="#fff"/></svg>I am a Tutor</a>

<h2 class="section-title abs" style="top:1685px">Students' Testimonials</h2>
<div class="title-rule abs" style="top:1737px"></div>
<div class="title-dot abs" style="top:1729px"></div>
<span class="quote-mark abs" style="left:78px;top:1748px">“</span>
<p class="quote abs">Fusce commodo tempus nibh, ac vestibulum odio ultricies ac. Interdum et malesuada fames ac ante ipsum primis in faucibus. Integer pharetra urna in sem varius hendrerit. Nunc vel nunc a massa auctor tristique vitae ac dolor. Praesent ac venenatis ipsum, quis pellentesque leo.</p>
<span class="quote-mark abs" style="left:1094px;top:1778px">”</span>
<div class="name-tag abs"><strong>Ravi Holland</strong><span>Florida</span></div>
<svg class="abs" style="left:590px;top:1895px" width="20" height="10" viewBox="0 0 20 10"><path d="M0 0H20L10 10Z" fill="#f26a21"/></svg>

<div class="avatar abs" style="left:82px;top:1975px;width:96px;height:96px;background:#c9b48a" role="img" aria-label="Student portrait"></div>
<div class="avatar abs" style="left:217px;top:1975px;width:96px;height:96px;background:#5e5e5e" role="img" aria-label="Student portrait"></div>
<div class="avatar abs" style="left:367px;top:1975px;width:96px;height:96px;background:#b5c2cc" role="img" aria-label="Student portrait"></div>
<div class="avatar abs" style="left:518px;top:1925px;width:164px;height:164px;background:var(--sky);border:6px solid #1f8fd8" role="img" aria-label="Featured student portrait"></div>
<div class="avatar abs" style="left:737px;top:1975px;width:96px;height:96px;background:#a7a98c" role="img" aria-label="Student portrait"></div>
<div class="avatar abs" style="left:887px;top:1975px;width:96px;height:96px;background:#6f6760" role="img" aria-label="Student portrait"></div>
<div class="avatar abs" style="left:1032px;top:1975px;width:96px;height:96px;background:#c7c3bd" role="img" aria-label="Student portrait"></div>

<section class="posts abs"></section>
<div class="post-col abs" style="left:80px">
  <h3>Articles From Our Tutors<span class="pager">‹›</span></h3>
  <div class="post"><div class="thumb" style="background:#f4e07a" role="img" aria-label="Sticky note reading helpful tips"></div><div><h4>Tips to Write an Awesome Thesis Statement</h4><p>Nam varius, enim ac vestibulum tincidunt, eros ligula dignissim nisl, sit amet commodo tellus quam ac libero.Nullam nec pharetra sapien, vitae laoreet est.</p><div class="by">By: Mira T</div></div></div>
  <div class="post"><div class="thumb" style="background:#f4e07a" role="img" aria-label="Sticky note reading helpful tips"></div><div><h4>Tips to Write an Awesome Thesis Statement</h4><p>Nam varius, enim ac vestibulum tincidunt, eros ligula dignissim nisl, sit amet commodo tellus quam ac libero.Nullam nec pharetra sapien, vitae laoreet est.</p><div class="by">By: Mira T</div></div></div>
</div>
<div class="post-col abs" style="left:635px">
  <h3>Blog<span class="pager">‹›</span></h3>
  <div class="post"><div class="thumb" style="background:#f3f3f3" role="img" aria-label="Colourful blog lettering"></div><div><h4>Tips to Write an Awesome Thesis Statement</h4><p>Nam varius, enim ac vestibulum tincidunt, eros ligula dignissim nisl, sit amet commodo tellus quam ac libero.Nullam nec pharetra sapien, vitae laoreet est.</p><div class="by">By: Mira T</div></div></div>
  <div class="post"><div class="thumb" style="background:#f3f3f3" role="img" aria-label="Colourful blog lettering"></div><div><h4>Tips to Write an Awesome Thesis Statement</h4><p>Nam varius, enim ac vestibulum tincidunt, eros ligula dignissim nisl, sit amet commodo tellus quam ac libero.Nullam nec pharetra sapien, vitae laoreet est.</p><div class="by">By: Mira T</div></div></div>
</div>

<h2 class="section-title abs" style="top:2610px">Our Partners</h2>
<div class="title-rule abs" style="top:2662px"></div>
<div class="title-dot abs" style="top:2654px"></div>
<span class="carousel-arrow abs" style="left:24px">‹</span>
<div class="partner abs" style="left:80px"><span></span></div>
<div class="partner abs" style="left:297px"><span></span></div>
<div class="partner abs" style="left:515px"><span></span></div>
<div class="partner abs" style="left:732px"><span></span></div>
<div class="partner abs" style="left:950px"><span></span></div>
<span class="carousel-arrow abs" style="left:1150px">›</span>

<footer class="site-footer abs"></footer>
<div class="foot-col abs" style="left:80px">
  <h4>Quick Links</h4>
  <ul><li>Home</li><li>About</li><li>How It Works</li><li>Students &amp;Parents</li><li>Tutors</li><li>Blog</li><li>Contact Us</li></ul>
</div>
<div class="foot-col abs" style="left:300px">
  <h4>Contact Information</h4>
  <div class="contact-row"><svg width="12" height="16" viewBox="0 0 12 16"><path d="M6 0a6 6 0 0 0-6 6c0 4 6 10 6 10s6-6 6-10a6 6 0 0 0-6-6z" fill="#fff"/><circle cx="6" cy="6" r="2" fill="#1566b4"/></svg><span>Lindenweg 14 4820 Halden,<br>Norway</span></div>
  <div class="contact-row"><svg width="12" height="14" viewBox="0 0 12 14"><path d="M2 0h3l1 4-2 1c1 2 2 3 4 4l1-2 4 1v3c0 1-1 2-2 2C5 13 0 8 0 2 0 1 1 0 2 0z" fill="#fff"/></svg><span>+40 (02) 555 018</span></div>
  <div class="contact-row"><svg width="14" height="10" viewBox="0 0 14 10"><rect width="14" height="10" fill="#fff"/><path d="M0 0l7 6 7-6" fill="none" stroke="#1566b4"/></svg><span>info@kx7orbit.com</span></div>
</div>
<div class="foot-col newsletter abs" style="left:640px">
  <h4>Newsletter Signup</h4>
  <p>Please enter your email address below to receive our FREE newsletter</p>
  <div class="field">Your Email ID</div>
  <a class="btn subscribe">SUBSCRIBE</a>
</div>
<div class="foot-col abs" style="left:935px">
  <h4>Follow Us</h4>
  <div class="social"><i></i>Friendwall</div>
  <div class="social"><i></i>Linkpro</div>
  <div class="social"><i></i>Chirper</div>
  <div class="social"><i></i>Email</div>
</div>
<div class="bottom-bar abs">
  <span class="copy">Copyright@Kx7Orbit.com, All Rights Are Reserved.</span>
  <span class="links"><span>Join Us</span><span>Login to Kx7Orbit Online</span><span>Remote Presentation/Support</span></span>
</div>

</body>
</html>
```